Classy, Elegant, Simple Business Card Design

Looking to have a classy, simple, and elegant design. Want a top notch designed business card. I really like the look of the new brivo credit card. I also like the design I attached. I am trying to reach 21-29 year old females for booking us for there wedding or event. We offer Disc Jockey Service, Photo Booth Rentals, and Uplighting .

Target Market(s)

21-28 year old females

Contact Information for Business Card

Has to have logo, website, email, and phone number

Font styles to use
Other font styles liked:
• open to font choice, modern, clean
Designer to choose
33a6d7
0791cd
0555a3
ffffff

Requirements
Must have
• Has to have logo, website, email, and phone number
Nice to have
• I really like the design of the new brivo credit card. I also included my logo and some designs I like
Should not have
• clutter or too much info

```html
<!DOCTYPE html>
<html lang="en">
<head>
<meta charset="utf-8">
<title>Tidewell Event Group – Business Card</title>
<link rel="stylesheet" href="https://fonts.googleapis.com/css2?family=Jost:wght@400;500&display=swap">
<style>
  :root {
    --backdrop: #d3d3d3;
    --card: #ffffff;
    --sky: #33a6d7;
    --azure: #0791cd;
    --royal: #0555a3;
    --ink: #1c2b4a;
    --muted: #9aa3ad;
  }
  * { box-sizing: border-box; margin: 0; padding: 0; }
  html, body { width: 1200px; height: 852px; overflow: hidden; }
  body {
    background: var(--backdrop);
    font-family: "Jost", sans-serif;
    position: relative;
  }
  .card {
    position: absolute;
    width: 560px;
    height: 320px;
    background: var(--card);
    border-radius: 22px;
    box-shadow: 0 4px 0 #e9e9e9, 0 7px 0 #c9c9c9, 0 14px 26px rgba(0,0,0,0.22);
  }
  .card--front { left: 70px; top: 70px; }
  .card--back { left: 570px; top: 440px; }

  .monogram {
    position: absolute;
    color: var(--azure);
    font-weight: 500;
    letter-spacing: 0.02em;
  }
  .card--front .monogram {
    left: 0; right: 0; top: 0; bottom: 0;
    display: flex; align-items: center; justify-content: center;
    font-size: 58px;
  }
  .card--back .monogram {
    left: 40px; top: 44px;
    font-size: 34px;
  }
  .wordmark {
    position: absolute;
    right: 40px; top: 40px;
    text-align: right;
    color: var(--royal);
    font-weight: 500;
    font-size: 24px;
    letter-spacing: 0.06em;
    text-transform: uppercase;
  }
  .contact {
    position: absolute;
    left: 40px; bottom: 34px;
    list-style: none;
    color: var(--ink);
    font-size: 17px;
    line-height: 1;
  }
  .contact li {
    display: flex; align-items: center; gap: 10px;
    margin-top: 10px;
  }
  .contact svg { width: 14px; height: 14px; flex: none; }
</style>
</head>
<body>
  <section class="card card--front" aria-label="Card front">
    <span class="monogram">Tidewell</span>
  </section>

  <section class="card card--back" aria-label="Card back">
    <span class="monogram">Tidewell</span>
    <span class="wordmark">Tidewell Event Group</span>
    <ul class="contact">
      <li>
        <svg viewBox="0 0 16 16" aria-hidden="true"><path fill="#0791cd" d="M4 1.5l2.2 3-1.3 1.6c.8 1.9 2.2 3.3 4 4.1l1.6-1.3 3 2.2-1 2.7c-6 .2-11.1-4.9-11.2-11.2z"/></svg>
        +1 555 204 7731
      </li>
      <li>
        <svg viewBox="0 0 16 16" aria-hidden="true"><rect x="1" y="3" width="14" height="10" rx="1" fill="#0791cd"/><path d="M1.5 3.8L8 9l6.5-5.2" fill="none" stroke="#fff" stroke-width="1.3"/></svg>
        info@tidewellevents.com
      </li>
      <li>
        <svg viewBox="0 0 16 16" aria-hidden="true"><circle cx="8" cy="8" r="7" fill="#0791cd"/><path d="M1 8h14M8 1c-3 3.5-3 10.5 0 14M8 1c3 3.5 3 10.5 0 14" fill="none" stroke="#fff" stroke-width="1"/></svg>
        www.tidewellevents.com
      </li>
    </ul>
  </section>
</body>
</html>
```